Harvest Bridge Brochure Design Project

We need a brochure that we can use to promote our education not-for-profit, Harvest Bridge Fund (www.harvestbridgeco.com) and promote our African bracelets that we are selling to fundraise for our organisation. The target audience is from high school to 40 years in the US and Australia.
Updates

Please find below the link to a new hi res logo. Thanks!
https://www.filecrate.net/s/9qm27vtrw84hzpa/Harvest_Bridge_logo_NEW.ai
https://www.filecrate.net/sh/3kd8wrx51bq2ve7/QPMNZRfo7Y

Reason: We have decided the final design to choose. Please give us a week to finalise.

Industry/Entity Type

High School

Requirements
Must have
• Photos of bracelets
Harvest Bridge logo
emotive photos of African students
A4 size with fold out features

```html
<!DOCTYPE html>
<html lang="en">
<head>
<meta charset="utf-8">
<title>Harvest Bridge Brochure</title>
<link rel="stylesheet" href="https://fonts.googleapis.com/css2?family=Arimo:wght@400;700&family=Roboto+Condensed:wght@400&family=Cinzel:wght@700&display=swap">
<style>
  :root {
    --stage: #141414;
    --green-deep: #138a35;
    --green-mid: #22a23f;
    --lime: #b8d432;
    --lime-soft: #cfe25a;
    --ink: #161616;
    --white: #ffffff;
    --caption: #d6d6d6;
    --leather-dark: #3e322a;
    --leather-warm: #6a4e3a;
  }
  * { box-sizing: border-box; margin: 0; padding: 0; }
  html, body { width: 1200px; height: 925px; overflow: hidden; }
  body {
    background: var(--stage);
    position: relative;
    font-family: "Arimo", Arial, sans-serif;
  }
  .panel {
    position: absolute;
    width: 441px;
    height: 661px;
    overflow: hidden;
  }
  .panel--back { left: 148px; top: 172px; background: var(--green-deep); }
  .panel--front { left: 631px; top: 99px; background: var(--lime); }

  .photo { position: absolute; left: 0; top: 0; width: 441px; }
  .photo--classroom {
    height: 450px;
    background: linear-gradient(180deg, #9fb6c4 0%, #8d9a6e 28%, #a79c82 55%, #5b5a4d 100%);
  }
  .photo--pupils {
    height: 400px;
    background: linear-gradient(180deg, #b7a98c 0%, #6f7a56 30%, #2f4a35 70%, #234031 100%);
  }
  .bands { position: absolute; left: 0; top: 0; width: 441px; height: 661px; }

  .brand {
    position: absolute;
    display: flex;
    align-items: center;
    gap: 8px;
    font-family: "Cinzel", Georgia, serif;
    font-weight: 700;
    font-size: 16px;
    line-height: 1.1;
  }
  .brand__dot { width: 12px; height: 12px; border-radius: 50%; flex: none; }
  .panel--back .brand { left: 52px; top: 586px; color: var(--lime-soft); }
  .panel--back .brand__dot { background: var(--lime-soft); }
  .panel--front .brand { left: 262px; top: 566px; color: var(--green-deep); }
  .panel--front .brand__dot { background: var(--green-deep); }

  .web { position: absolute; font-size: 12.5px; }
  .panel--back .web { left: 40px; top: 630px; width: 180px; text-align: center; color: var(--white); }
  .panel--front .web { left: 254px; top: 614px; width: 150px; text-align: center; color: var(--ink); }

  .contact {
    position: absolute;
    left: 235px;
    top: 486px;
    color: var(--white);
    font-size: 8.6px;
    line-height: 10.6px;
  }
  .contact__title { font-size: 10.5px; line-height: 12px; }
  .contact__region { font-weight: 700; font-size: 11px; line-height: 12px; }
  .contact__region--spaced { margin-top: 10px; font-size: 12px; }

  .bracelets {
    position: absolute;
    left: 42px;
    top: 406px;
    width: 232px;
    height: 64px;
    border-radius: 6px;
    background: linear-gradient(100deg, var(--leather-dark) 0%, var(--leather-warm) 60%, #8a5e3e 100%);
  }
  .headline {
    position: absolute;
    left: 44px;
    top: 504px;
    width: 178px;
    font-size: 18px;
    line-height: 24px;
    font-weight: 700;
    color: var(--ink);
  }

  .caption {
    position: absolute;
    font-family: "Roboto Condensed", "Arial Narrow", sans-serif;
    font-size: 14.5px;
    color: var(--caption);
    letter-spacing: 0.3px;
    width: 441px;
    text-align: center;
  }
  .caption--back { left: 148px; top: 848px; }
  .caption--front { left: 631px; top: 775px; }
</style>
</head>
<body>

  <section class="panel panel--back">
    <div class="photo photo--classroom" role="img" aria-label="Photo of a teacher leading an outdoor class of African schoolchildren in green uniforms under trees"></div>
    <svg class="bands" viewBox="0 0 441 661" aria-hidden="true">
      <defs>
        <linearGradient id="backGreen" x1="0" y1="0" x2="0" y2="1">
          <stop offset="0" stop-color="#22a23f"/>
          <stop offset="1" stop-color="#12862f"/>
        </linearGradient>
      </defs>
      <path d="M0 410 Q200 445 441 392 L441 418 Q220 470 0 432 Z" fill="#b8d432"/>
      <path d="M0 430 Q220 468 441 416 L441 661 L0 661 Z" fill="url(#backGreen)"/>
    </svg>
    <div class="brand"><span class="brand__dot"></span><span>Harvest Bridge<br>Foundation</span></div>
    <p class="web">www.harvestbridgeco.com</p>
    <div class="contact">
      <p class="contact__title">Contact Us</p>
      <p class="contact__region">USA</p>
      <p>Harvest Bridge Fund</p>
      <p>88 Larkspur Avenue – Suite 240</p>
      <p>New York, NY 10014</p>
      <p class="contact__region contact__region--spaced">Australia</p>
      <p>Harvest Bridge Fund</p>
      <p>P.O. Box 512</p>
      <p>Fernbrook NSW 2031</p>
      <p>Phone</p>
      <p>United States: +1 555 014 2290</p>
      <p>Australia: +61 400 555 318</p>
      <p>Email: support@harvestbridgeco.org</p>
    </div>
  </section>

  <section class="panel panel--front">
    <div class="photo photo--pupils" role="img" aria-label="Photo of smiling African schoolchildren in green uniforms waving at the camera"></div>
    <svg class="bands" viewBox="0 0 441 661" aria-hidden="true">
      <defs>
        <linearGradient id="frontLime" x1="0" y1="0" x2="0" y2="1">
          <stop offset="0" stop-color="#c2da3c"/>
          <stop offset="1" stop-color="#aacc2a"/>
        </linearGradient>
      </defs>
      <path d="M0 392 Q200 355 441 398 L441 425 Q220 385 0 410 Z" fill="#138a35"/>
      <path d="M0 408 Q220 382 441 423 L441 661 L0 661 Z" fill="url(#frontLime)"/>
    </svg>
    <div class="bracelets" role="img" aria-label="Photo of three handmade leather bracelets"></div>
    <h1 class="headline">How many people can actually say they helped build a school in Africa? - You Can!</h1>
    <div class="brand"><span class="brand__dot"></span><span>Harvest Bridge<br>Foundation</span></div>
    <p class="web">www.harvestbridgeco.com</p>
  </section>

  <p class="caption caption--back">BROCHURE - BACK</p>
  <p class="caption caption--front">BROCHURE - FRONT</p>

</body>
</html>
```